Harbor Summit Flyer

We need a company flyer to present our company. Target group: Senior managers of hospitals / care facilities.
Please use the new text from the document "Kongressflyer.pptx".
Design: The last flyer can be used as a design basis - attached here: "Blue Lantern Flyer High Res Compressed.pdf". Please note the layout of the business card. The flyer must visually match the business card.
Logos for the references attached (KTV, Pelmora, Wendlach, Tarnford, Am Blauen Tor, Brunnwerk, Voli, KMBT).
Format: DIN A long in portrait format, front and back printed (or open to alternative suggestions if the format does not appear optimal from a design point of view)
Timing: We need the flyer as soon as possible

```html
<!DOCTYPE html>
<html lang="de">
<head>
<meta charset="utf-8">
<title>Blue Lantern Flyer</title>
<link rel="stylesheet" href="https://fonts.googleapis.com/css2?family=Abril+Fatface&family=Source+Sans+3:wght@400;600;700&display=swap">
<style>
:root{
  --stage:#3d3d3d;
  --paper:#f6f6f6;
  --teal:#2d6b82;
  --teal-deep:#1e4d66;
  --navy:#1d3f5a;
  --red:#e5473a;
  --red-deep:#d23a30;
  --ink:#2e2e2e;
  --white:#ffffff;
  --serif:'Abril Fatface', Georgia, serif;
  --sans:'Source Sans 3', Arial, sans-serif;
}
*{box-sizing:border-box;margin:0;padding:0}
html,body{width:900px;height:1200px;overflow:hidden;background:var(--stage)}
.flyer{position:absolute;left:60px;top:48px;width:780px;height:1104px;background:var(--paper);font-family:var(--sans);color:var(--ink);overflow:hidden}
.abs{position:absolute}

.brand{left:0;right:0;top:34px;text-align:center;font-family:var(--sans);font-weight:400;font-size:22px;letter-spacing:4px;color:var(--teal-deep)}
.brand .dot{display:inline-block;width:10px;height:10px;border-radius:50%;background:var(--teal);margin-right:10px;vertical-align:middle}

.intro{left:0;top:98px;width:780px;height:196px;background:linear-gradient(115deg,#2f7088 0%,#245e78 45%,#1e4f6a 100%);color:var(--white)}
.intro-text{left:212px;top:24px;font-size:15px;line-height:26px}
.intro-text .bullet{position:relative;padding-left:18px}
.intro-text .bullet::before{content:"";position:absolute;left:0;top:9px;width:9px;height:9px;border-radius:50%;background:var(--red)}
.headline{left:0;right:0;top:140px;text-align:center;font-family:var(--serif);font-size:33px;letter-spacing:.5px}

.tab{left:294px;top:294px;width:186px;height:37px;background:var(--red);color:var(--white);font-family:var(--serif);font-size:16px;text-align:center;line-height:37px}
.about{left:46px;top:344px;width:697px;font-size:11.5px;line-height:12px;text-align:justify}
.about strong{color:var(--red);font-weight:600}

.label{left:207px;top:408px;width:484px;height:40px;background:var(--teal);color:var(--white);font-family:var(--serif);font-size:15px;text-align:center;line-height:40px}

.col{width:340px;font-size:11.5px;line-height:22px}
.col-left{left:41px;top:474px}
.col-right{left:425px;top:470px}
.divider{left:401px;top:470px;width:1px;height:150px;background:#b9c6cd}
.point{position:relative;padding-left:20px;color:var(--red);font-weight:600;font-size:14px;line-height:22px;margin-top:6px}
.point::before{content:"";position:absolute;left:2px;top:7px;width:9px;height:9px;border-radius:50%;background:var(--teal)}
.sub{padding-left:20px;line-height:16px}
.sub.dot{position:relative}
.sub.dot::before{content:"";position:absolute;left:3px;top:4px;width:8px;height:8px;border-radius:50%;background:var(--red)}
.sub + .sub{margin-top:6px}

.positions-rule{left:0;top:643px;width:780px;height:4px;background:var(--navy)}
.contact-panel{left:469px;top:647px;width:311px;height:367px;background:linear-gradient(150deg,#ec5a48 0%,var(--red) 45%,var(--red-deep) 100%)}
.bottom-rule{left:0;top:1012px;width:780px;height:3px;background:var(--navy)}

.pos-head{left:41px;top:670px;font-family:var(--serif);font-size:21px;line-height:26px}
.pos-head .r{color:var(--red)}
.pos-head .t{color:var(--teal-deep);padding-left:14px}
.pos-list{left:41px;top:734px;width:400px;font-size:11.5px}
.pos-list .lead{position:relative;padding-left:22px;line-height:15px}
.pos-list .lead::before{content:"";position:absolute;left:2px;top:2px;width:9px;height:9px;border-radius:50%;background:var(--teal)}
.pos-list ul{list-style:none;margin:12px 0 0}
.pos-list li{position:relative;padding-left:22px;line-height:24px}
.pos-list li::before{content:"";position:absolute;left:3px;top:8px;width:8px;height:8px;border-radius:50%;background:var(--teal-deep)}
.pos-list .group{margin-top:10px;font-weight:700;letter-spacing:.3px;padding-left:22px;position:relative;line-height:18px}
.pos-list .group::before{content:"";position:absolute;left:2px;top:5px;width:9px;height:9px;border-radius:50%;background:var(--teal)}
.pos-list .lead.second{margin-top:12px}

.person{left:438px;width:330px;height:100px}
.person .photo{position:absolute;left:0;top:0;width:96px;height:96px;border-radius:50%;border:3px solid var(--white);background:radial-gradient(circle at 50% 40%,#8a7f78 0%,#3b3532 60%,#1f1c1b 100%)}
.person .name{position:absolute;left:129px;top:6px;font-family:var(--serif);font-size:13px;color:var(--white);line-height:15px;letter-spacing:.3px}
.person .line{position:absolute;left:129px;font-size:14px;font-weight:600;color:var(--white);display:flex;align-items:center;gap:8px}
.person .icon{width:16px;height:16px;border-radius:50%;background:var(--white);display:flex;align-items:center;justify-content:center}

.partners{left:0;top:1015px;width:780px;height:89px;background:var(--white)}
.partner{position:absolute;top:38px;font-size:11px;font-weight:600;color:var(--teal-deep)}
.partner.mark{display:flex;align-items:center;gap:5px}
.partner.mark::before{content:"";width:10px;height:10px;border-radius:50%;background:var(--teal)}
.partner-client{position:absolute;left:600px;top:26px;font-size:28px;font-weight:700;color:#23a6a0}
</style>
</head>
<body>
<main class="flyer">

  <header class="brand abs"><span class="dot"></span>BLUE LANTERN</header>

  <section class="intro abs">
    <div class="intro-text abs">
      <p>Sie sind Leiter eines Krankenhauses und suchen…</p>
      <p class="bullet">medizinische Fachkräfte für Ihre Klinik oder</p>
      <p class="bullet">herausragende Führungskräfte für Ihre Klinikverwaltung?</p>
      <p>Möchten Sie dabei auf Augenhöhe begleitet werden?</p>
    </div>
    <h1 class="headline abs">WIR UNTERSTÜTZEN SIE GERNE.</h1>
  </section>

  <h2 class="tab abs">WER SIND WIR?</h2>
  <p class="about abs">Seit fast <strong>30 JAHREN</strong> gehört das Unternehmen Varnholt / Blue Lantern zu den bedeutensten Personalberatungen im Gesundheitswesen. Die Rekrutierung von Spitzenpersonal für Kliniken ist unsere große Leidenschaft. Durch den Zusammenschluss der beiden Firmen haben wir uns im letzten Jahr modernisiert, digitalisiert und für die Zukunft aufgestellt – ohne dabei die Tradition aus den Augen zu verlieren.</p>

  <h2 class="label abs">WARUM KÖNNEN WIR SIE BESTMÖGLICH UNTERSTÜTZEN?</h2>

  <div class="col col-left abs">
    <p class="point">Ehrlichkeit ist uns wichtig …</p>
    <p class="sub dot">bei uns bekommen Sie aufrichtiges Marktfeedback und</p>
    <p class="sub dot">garantiert keine Versprechungen, die wir nicht<br>halten können</p>
    <p class="point">Wir lieben was wir tun …</p>
    <p class="sub">und wir arbeiten schnell, effizient und auf Augenhöhe</p>
  </div>
  <div class="divider abs"></div>
  <div class="col col-right abs">
    <p class="point">Wir sind Spezialisten im Gesundheitswesen …</p>
    <p class="sub">unser Team verfügt über fundiertes Marktverständnis</p>
    <p class="point">Überragendes Netzwerk …</p>
    <p class="sub">in allen Teilsektoren des Gesundheitswesens<br>Digital …<br>unsere Prozesse? Transparent! Unsere Suche für Sie <strong>24/7<br>EINSEHBAR</strong></p>
  </div>

  <div class="positions-rule abs"></div>
  <div class="contact-panel abs"></div>

  <h2 class="pos-head abs"><span class="r">WAS SIND TYPISCHE POSITIONEN,</span><br><span class="t">DIE WIR BESETZEN?</span></h2>
  <div class="pos-list abs">
    <p class="lead">100 Besetzungen in vergangenen 2 Jahren <strong>in sämtlichen<br>Fachrichtungen</strong>, z.B.</p>
    <ul>
      <li>Chefarzt Gynäkologie / Geburtshilfe</li>
      <li>Chefarzt Radiologie</li>
      <li>Chefarzt Psychiatrie</li>
    </ul>
    <p class="group">HERAUSRAGENDE FÜHRUNGSKRÄFTE</p>
    <p class="lead second"><strong>150 Besetzungen von Leitungspositionen in sämtlichen<br>Geschäftsbereichen</strong> in vergangenen 2 Jahren, z.B.<br>Klinik Geschäftsführung / Vorstände</p>
    <ul>
      <li>Leitung Personal</li>
      <li>Leitung Qualitäts- und Risikomanagement</li>
      <li>Leitung Patientenmanagement</li>
    </ul>
  </div>

  <div class="person abs" style="top:676px">
    <div class="photo" role="img" aria-label="Porträtfoto der Beraterin Dr. med. Carla Brenning-Hoff"></div>
    <p class="name">DR. MED CARLA BRENNING-<br>HOFF</p>
    <p class="line" style="top:46px"><span class="icon"><svg width="9" height="9" viewBox="0 0 10 10"><path d="M2 1l2 2-1 1.2c.6 1.2 1.6 2.2 2.8 2.8L7 6l2 2-1.3 1.3C4.6 9 1 5.4.7 2.3z" fill="#e5473a"/></svg></span>+49 170 5550142</p>
    <p class="line" style="top:68px"><span class="icon"><svg width="9" height="9" viewBox="0 0 10 10"><rect x="1" y="2.5" width="8" height="5.5" fill="#e5473a"/><path d="M1 2.5l4 3 4-3" stroke="#fff" fill="none"/></svg></span>cbh@bluelantern.example</p>
  </div>

  <div class="person abs" style="top:786px">
    <div class="photo" role="img" aria-label="Porträtfoto der Beraterin Mara Lintner"></div>
    <p class="name">MARA LINTNER</p>
    <p class="line" style="top:32px"><span class="icon"><svg width="9" height="9" viewBox="0 0 10 10"><path d="M2 1l2 2-1 1.2c.6 1.2 1.6 2.2 2.8 2.8L7 6l2 2-1.3 1.3C4.6 9 1 5.4.7 2.3z" fill="#e5473a"/></svg></span>+43 660 5550178</p>
    <p class="line" style="top:54px"><span class="icon"><svg width="9" height="9" viewBox="0 0 10 10"><rect x="1" y="2.5" width="8" height="5.5" fill="#e5473a"/><path d="M1 2.5l4 3 4-3" stroke="#fff" fill="none"/></svg></span>ml@bluelantern.example</p>
  </div>

  <div class="person abs" style="top:902px">
    <div class="photo" role="img" aria-label="Porträtfoto des Beraters Jonas Reuter"></div>
    <p class="name">JONAS REUTER</p>
    <p class="line" style="top:32px"><span class="icon"><svg width="9" height="9" viewBox="0 0 10 10"><path d="M2 1l2 2-1 1.2c.6 1.2 1.6 2.2 2.8 2.8L7 6l2 2-1.3 1.3C4.6 9 1 5.4.7 2.3z" fill="#e5473a"/></svg></span>+49 171 5550193</p>
    <p class="line" style="top:54px"><span class="icon"><svg width="9" height="9" viewBox="0 0 10 10"><rect x="1" y="2.5" width="8" height="5.5" fill="#e5473a"/><path d="M1 2.5l4 3 4-3" stroke="#fff" fill="none"/></svg></span>jr@bluelantern.example</p>
  </div>

  <div class="bottom-rule abs"></div>

  <footer class="partners abs">
    <span class="partner mark" style="left:40px">Voli</span>
    <span class="partner mark" style="left:130px">Parvelis</span>
    <span class="partner" style="left:222px">Orvena</span>
    <span class="partner mark" style="left:300px">Pelmora</span>
    <span class="partner" style="left:388px">Lindhaus</span>
    <span class="partner" style="left:466px">Talgrund</span>
    <span class="partner-client">Varnholt</span>
  </footer>

</main>
</body>
</html>
```